Communication of Recommended Belief Letter

To Whom This May Concern,

My company's name is Bramwell LLC. I would like to send electronic messages to my clients. Therefore, I would like PixelHarbor to create a letterhead template to say Bramwell- without the LLC. My messages could extend up to 20 pages long. I would like something that is chic, fancy, and has creative designs. The background color should be white. The creative designs are open for suggestions without color restrictions. Font type and color are also open for suggestions. It may be what you believe best suite's the letterhead. I would like the letterhead to include the company logo. Please see attachment for file. Thank you.

Target Market(s)

working class American's

Industry/Entity Type

Communication

Contact Information for Business Card

The business card should be chic and fancy.

Font styles to use
Script

Requirements
Must have
• Company name: Bramwell LLC
• Company symbol: Please see attachment
• Name: Marisol Denby
• Title: President
• Company website: www.bramwellllc-example.com
Nice to have
• Open for suggestions

```html
<!DOCTYPE html>
<html lang="en">
<head>
<meta charset="utf-8">
<title>Bramwell Letterhead</title>
<link href="https://fonts.googleapis.com/css2?family=Cinzel:wght@400&family=Open+Sans:wght@400;600&display=swap" rel="stylesheet">
<style>
  :root {
    --backdrop: #ecebe8;
    --paper: #ffffff;
    --teal: #437c84;
    --teal-dark: #3a6f77;
    --charcoal: #474848;
    --charcoal-edge: #5e5f5f;
    --gold: #c99a2e;
    --ink: #2a2a2a;
    --ghost: #f6f1e4;
  }
  * { margin: 0; padding: 0; box-sizing: border-box; }
  html, body {
    width: 1200px;
    height: 1200px;
    overflow: hidden;
    background: var(--backdrop);
  }
  .letterhead {
    position: absolute;
    left: 210px;
    top: 48px;
    width: 779px;
    height: 1103px;
    background: var(--paper);
    box-shadow: 0 10px 30px rgba(0,0,0,0.18);
    overflow: hidden;
  }
  .frame {
    position: absolute;
    inset: 0;
    width: 100%;
    height: 100%;
  }
  .brand {
    position: absolute;
    left: 60px;
    top: 42px;
    display: flex;
    align-items: center;
    gap: 40px;
  }
  .brand-dot {
    width: 90px;
    height: 90px;
    border-radius: 50%;
    background: var(--gold);
  }
  .brand-name {
    font-family: "Cinzel", serif;
    font-weight: 400;
    font-size: 50px;
    letter-spacing: 1px;
    color: var(--ink);
  }
  .watermark-name {
    position: absolute;
    left: 0;
    right: 0;
    top: 560px;
    text-align: center;
    font-family: "Cinzel", serif;
    font-weight: 400;
    font-size: 80px;
    color: var(--ghost);
  }
  .signature {
    position: absolute;
    right: 22px;
    bottom: 8px;
    text-align: center;
    font-family: "Open Sans", sans-serif;
    color: #111;
    line-height: 1.15;
  }
  .signature-title { font-size: 20px; font-weight: 400; }
  .signature-name { font-size: 18px; font-weight: 400; }
  .signature-web { font-size: 10.5px; color: #333; margin-top: 3px; }
</style>
</head>
<body>
  <main class="letterhead">
    <svg class="frame" viewBox="0 0 779 1103" aria-hidden="true">
      <path class="corner-edge" d="M505 0 C632 40 735 140 779 262 L779 0 Z" fill="var(--charcoal-edge)"/>
      <path class="corner" d="M513 0 C640 38 742 136 779 255 L779 0 Z" fill="var(--charcoal)"/>
      <path class="side-band" d="M0 122 L30 122 Q62 122 62 154 L62 1042 L435 1042 Q492 1042 507 1103 L0 1103 Z" fill="var(--teal)"/>
      <path class="side-band-shade" d="M0 1048 L62 1048 L62 1042 L435 1042 Q492 1042 507 1103 L0 1103 Z" fill="var(--teal-dark)" opacity="0.35"/>
    </svg>

    <header class="brand">
      <span class="brand-dot"></span>
      <span class="brand-name">Bramwell</span>
    </header>

    <div class="watermark-name">Bramwell</div>

    <footer class="signature">
      <div class="signature-title">President</div>
      <div class="signature-name">MARISOL DENBY</div>
      <div class="signature-web">www.bramwellllc-example.com</div>
    </footer>
  </main>
</body>
</html>
```